Letterhead Design Project

Looking for letterhead designs for Brastova Mining.

I am looking for a letterhead design in conjunction with a business card design. I have opened contests for both but ask that if you submit a letterhead design you also submit a business card design with a corresponding look/feel.

Brastova Mining is a B2B company that buys and sells large machinery tires within the coal mining industry. The design should the strong, crisp and masculine. I have uploaded the company logo and mock-up of the back of the company's business card.

Color scheme should be grey/green/black

Contact information to include:
Name: Dale Whitford
Title: Managing Director
Phone: 555-231-4097
Address: 1817 Pellam #3 Dallas, TX 75290
Email: Dale@Brastova.example
Updates

Project Deadline Extended
Reason: Looking for a more refined, elegant letterhead than what's been submitted as of yet. Here is a sample of what we're looking for: http://www.plumcrestgallery.example/letterhead-designs/ We will also be increasing the payment.

Industry/Entity Type

Coal Mining

```html
<!DOCTYPE html>
<html lang="en">
<head>
<meta charset="utf-8">
<title>Brastova Mining — Letterhead and Business Card</title>
<link href="https://fonts.googleapis.com/css2?family=Libre+Baskerville:wght@700&family=Questrial&display=swap" rel="stylesheet">
<style>
  :root {
    --page: #ffffff;
    --sheet-edge: #4a4a4a;
    --metal-dark: #1e1f20;
    --metal-mid: #3a3b3d;
    --brand-green: #8fd13a;
    --footer-text: #8c8c8c;
    --card-text: #d4bcbc;
    --label-text: #111111;
  }
  * { box-sizing: border-box; margin: 0; padding: 0; }
  html, body {
    width: 1139px;
    height: 1200px;
    overflow: hidden;
    background: var(--page);
  }
  .canvas {
    position: relative;
    width: 1139px;
    height: 1200px;
    background: var(--page);
  }

  .proof-label {
    position: absolute;
    top: 14px;
    right: 24px;
    text-align: right;
    font-family: "Questrial", sans-serif;
    font-size: 14px;
    line-height: 18px;
    color: var(--label-text);
  }
  .proof-label .date { margin-bottom: 18px; }

  .metal-texture {
    position: absolute;
    inset: 0;
    background: linear-gradient(180deg, var(--metal-mid) 0%, var(--metal-dark) 100%);
  }

  /* Letterhead */
  .letterhead {
    position: absolute;
    left: 10px;
    top: 215px;
    width: 745px;
    height: 965px;
    border: 1px solid var(--sheet-edge);
    background: var(--page);
  }
  .letterhead-header {
    position: absolute;
    left: 0; top: 0;
    width: 100%;
    height: 91px;
  }
  .letterhead-footer {
    position: absolute;
    left: 0; bottom: 0;
    width: 100%;
    height: 43px;
    overflow: hidden;
  }

  .wordmark {
    position: absolute;
    left: 0; right: 0;
    text-align: center;
    font-family: "Libre Baskerville", serif;
    font-weight: 700;
    color: var(--brand-green);
    text-transform: uppercase;
  }
  .wordmark .name { display: block; }
  .wordmark .sector { display: block; }

  .letterhead-header .wordmark { top: 14px; }
  .letterhead-header .wordmark .name { font-size: 44px; line-height: 50px; letter-spacing: 1px; }
  .letterhead-header .wordmark .sector { font-size: 12px; line-height: 14px; letter-spacing: 18px; padding-left: 18px; }

  .footer-contact {
    position: absolute;
    left: 12px; right: 12px;
    top: 15px;
    text-align: center;
    font-family: "Libre Baskerville", serif;
    font-weight: 700;
    font-size: 9.2px;
    line-height: 13px;
    letter-spacing: 0;
    color: var(--footer-text);
    text-transform: uppercase;
    white-space: nowrap;
  }

  /* Business card */
  .business-card {
    position: absolute;
    left: 802px;
    top: 530px;
    width: 307px;
    height: 175px;
    border: 1px solid var(--sheet-edge);
    overflow: hidden;
  }
  .business-card .wordmark { top: 16px; }
  .business-card .wordmark .name { font-size: 40px; line-height: 44px; letter-spacing: 1px; }
  .business-card .wordmark .sector { font-size: 10px; line-height: 12px; letter-spacing: 14px; padding-left: 14px; }

  .card-contact {
    position: absolute;
    left: 0; right: 0;
    top: 100px;
    text-align: center;
    font-family: "Libre Baskerville", serif;
    font-weight: 700;
    color: var(--card-text);
  }
  .card-contact .person { font-size: 9.5px; line-height: 11px; text-transform: uppercase; }
  .card-contact .title { font-size: 7px; line-height: 10px; margin-bottom: 5px; }
  .card-contact .line { font-size: 7.5px; line-height: 14px; letter-spacing: 0.6px; }
</style>
</head>
<body>
<div class="canvas">

  <div class="proof-label">
    <p class="date">10–5–13</p>
    <p>BRASTOVA MINING_v1</p>
    <p>LOGO PROOF</p>
    <p>BUSINESS CARD PROOF</p>
    <p>LETTER HEAD PROOF</p>
  </div>

  <section class="letterhead">
    <header class="letterhead-header">
      <div class="metal-texture" role="img" aria-label="Dark perforated metal plate texture"></div>
      <div class="wordmark">
        <span class="name">Brastova</span>
        <span class="sector">Mining</span>
      </div>
    </header>
    <footer class="letterhead-footer">
      <div class="metal-texture" role="img" aria-label="Dark perforated metal plate texture"></div>
      <p class="footer-contact">Dale Whitford | Managing Director | 1817 Pellam #3 Dallas, TX 75290 | 555-231-4097 | Dale@Brastova.example</p>
    </footer>
  </section>

  <section class="business-card">
    <div class="metal-texture" role="img" aria-label="Dark perforated metal plate texture"></div>
    <div class="wordmark">
      <span class="name">Brastova</span>
      <span class="sector">Mining</span>
    </div>
    <div class="card-contact">
      <p class="person">Dale Whitford</p>
      <p class="title">managing director</p>
      <p class="line">1817 Pellam #3. Dallas, TX 75290</p>
      <p class="line">555.231.4097</p>
      <p class="line">dale@brastova.example</p>
    </div>
  </section>

</div>
</body>
</html>
```